Flyer Design

I'm looking for a new flyer design to help promote our landscape company, and some of our main service for the up and coming season. We're trying to position ourselves as a leader in our market, so obviously quality is important to us.

Our current promotion is 25% off the first month with signup of annual service.

Phone Number: (816) 555-0193
Website: gardelvista.com
Our tagline: "Your hands are full... Let us help"

The call to action: direct them to our website for a detailed list of services and to receive a free quote.

You're welcome to add your own wording and punctuation. If I like the design I will provide feedback accordingly.

I have attached a jpg of our logo to help with design colors. I will provide the vector file upon completion of this project.

Also, I've attached a few photos that I had on hand of our companies work that may help with the design. Obviously I don't want to use them all, but there are a couple just to help out. I'm not opposed to stock photos either.
Thanks

Target Market(s)

We market to high end customers, generally with home between $500k-$2mil, or household income over $200k. Quality and creativity are most important to us.

Industry/Entity Type

Landscape

Requirements
Must have
• Creativity, easy to read, modern style.

```html
<!DOCTYPE html>
<html lang="en">
<head>
<meta charset="utf-8">
<title>Gardel Vista – Flyer</title>
<link rel="stylesheet" href="https://fonts.googleapis.com/css2?family=Oswald:wght@500;700&family=Roboto+Condensed:ital,wght@0,700;1,800&family=Roboto:wght@700&display=swap">
<style>
  :root {
    --orange: #e2542a;
    --orange-deep: #b83a18;
    --orange-text: #f26a2a;
    --charcoal: #232323;
    --charcoal-soft: #3a3a3a;
    --white: #ffffff;
    --silver: #d9d9d9;
    --photo-dark: #3b2a2a;
    --photo-light: #cfd3d8;
  }
  * { margin: 0; padding: 0; box-sizing: border-box; }
  html, body { width: 900px; height: 1200px; overflow: hidden; background: #f2f2f2; }
  .flyer {
    position: relative;
    width: 900px; height: 1200px; overflow: hidden;
    background: radial-gradient(ellipse at 50% 55%, #ee6434 0%, var(--orange) 45%, var(--orange-deep) 100%);
    font-family: "Roboto", Arial, sans-serif;
  }
  .hero-photo { position: absolute; inset: 0; width: 900px; height: 520px; }
  .brand-badge {
    position: absolute; left: 45px; top: 45px;
    width: 240px; height: 240px; border-radius: 50%;
    background: var(--white);
    display: flex; align-items: center; justify-content: center;
    box-shadow: 0 4px 14px rgba(0,0,0,.35);
  }
  .brand-name {
    font-family: "Oswald", sans-serif; font-weight: 700;
    font-size: 40px; color: var(--charcoal); text-transform: uppercase;
    text-align: center; line-height: 1.05;
  }
  .tagline-box {
    position: absolute; left: 185px; top: 402px; width: 530px; height: 168px;
    border-radius: 22px;
    background: linear-gradient(180deg, #4a4a4a, #1e1e1e);
    border: 6px solid var(--silver);
    box-shadow: 0 6px 14px rgba(0,0,0,.45);
    text-align: center;
  }
  .tagline-lead {
    margin-top: 14px;
    font-family: "Roboto Condensed", sans-serif; font-style: italic; font-weight: 800;
    font-size: 34px; color: var(--white); letter-spacing: .5px;
  }
  .tagline-main {
    font-family: "Oswald", sans-serif; font-weight: 500;
    font-size: 88px; line-height: 1; color: var(--orange-text);
  }
  .services-pill {
    position: absolute; left: 350px; top: 570px; width: 200px; height: 50px;
    border-radius: 25px; background: #111;
    color: var(--white); text-align: center; line-height: 50px;
    font-family: "Roboto Condensed", sans-serif; font-style: italic; font-weight: 800; font-size: 32px;
  }
  .services-band {
    position: absolute; left: 0; top: 650px; width: 900px; height: 270px;
    display: flex;
    background: linear-gradient(180deg, #2c2c2c, #151515);
    box-shadow: 0 6px 12px rgba(0,0,0,.4);
  }
  .service {
    flex: 1; display: flex; flex-direction: column; align-items: center;
    border-right: 2px solid #111;
    background: linear-gradient(90deg, #1d1d1d, #343434);
  }
  .service:last-child { border-right: none; }
  .service-name {
    height: 80px; display: flex; align-items: center; justify-content: center;
    text-align: center; color: var(--white); font-size: 21px; line-height: 1.15;
    padding-top: 18px;
  }
  .service-icon { width: 124px; height: 124px; margin-top: 12px; }
  .promo {
    position: absolute; left: 0; width: 900px; top: 948px;
    display: flex; justify-content: center; align-items: center; gap: 6px;
    font-family: "Roboto Condensed", sans-serif; font-weight: 700; color: #f4f4f4;
    text-shadow: 0 3px 4px rgba(0,0,0,.45);
  }
  .promo-value { font-size: 84px; line-height: 1; }
  .promo-off {
    font-size: 30px; writing-mode: vertical-rl; transform: rotate(180deg);
    letter-spacing: 2px; line-height: 1;
  }
  .promo-rest { font-size: 84px; line-height: 1; }
  .contact-arc { position: absolute; left: 0; top: 1060px; width: 900px; height: 140px; }
  .contact {
    position: absolute; left: 0; width: 900px; top: 1090px; text-align: center;
  }
  .contact-phone { color: var(--orange-text); font-size: 30px; }
  .contact-web { color: var(--white); font-size: 30px; margin-top: 6px; }
</style>
</head>
<body>
<main class="flyer">
  <svg class="hero-photo" viewBox="0 0 900 520" role="img" aria-label="Photo of a red pickup truck with a snow plow clearing snow">
    <defs>
      <linearGradient id="heroFill" x1="0" y1="0" x2="1" y2="1">
        <stop offset="0" stop-color="var(--photo-light)"/>
        <stop offset=".45" stop-color="#6a3434"/>
        <stop offset="1" stop-color="var(--photo-dark)"/>
      </linearGradient>
    </defs>
    <path d="M0 0 H900 V300 C860 430 720 470 560 470 H330 C180 470 60 420 0 330 Z" fill="url(#heroFill)"/>
    <path d="M0 330 C60 420 180 470 330 470 H560 C720 470 860 430 900 300" fill="none" stroke="var(--white)" stroke-width="10"/>
  </svg>

  <div class="brand-badge"><span class="brand-name">Gardel<br>Vista</span></div>

  <section class="tagline-box">
    <p class="tagline-lead">YOUR HANDS ARE FULL...</p>
    <p class="tagline-main">LET US HELP</p>
  </section>

  <div class="services-pill">SERVICES</div>

  <section class="services-band">
    <div class="service">
      <p class="service-name">MOWING</p>
      <svg class="service-icon" viewBox="0 0 124 124">
        <circle cx="62" cy="62" r="60" fill="var(--orange)"/>
        <g fill="none" stroke="var(--charcoal)" stroke-width="5" stroke-linecap="round">
          <line x1="30" y1="34" x2="58" y2="70"/>
        </g>
        <path d="M50 68 H88 L92 80 H46 Z" fill="var(--charcoal)"/>
        <circle cx="52" cy="86" r="8" fill="var(--charcoal)"/>
        <circle cx="86" cy="86" r="8" fill="var(--charcoal)"/>
      </svg>
    </div>
    <div class="service">
      <p class="service-name">TREE<br>MAINTENANCE</p>
      <svg class="service-icon" viewBox="0 0 124 124">
        <circle cx="62" cy="62" r="60" fill="var(--orange)"/>
        <g fill="none" stroke="var(--charcoal)" stroke-width="4" stroke-linejoin="round">
          <path d="M42 70 C28 66 28 46 42 44 C42 30 60 24 66 34 C78 26 94 38 88 50 C98 58 90 74 78 70 Z"/>
          <path d="M58 98 V70 M66 98 V70 M62 72 L52 58 M62 72 L74 56"/>
        </g>
      </svg>
    </div>
    <div class="service">
      <p class="service-name">AERATION</p>
      <svg class="service-icon" viewBox="0 0 124 124">
        <circle cx="62" cy="62" r="60" fill="var(--orange)"/>
        <g fill="var(--charcoal)">
          <circle cx="46" cy="34" r="3.5"/><circle cx="56" cy="34" r="3.5"/><circle cx="68" cy="34" r="3.5"/><circle cx="78" cy="34" r="3.5"/>
          <circle cx="46" cy="46" r="3.5"/><circle cx="56" cy="46" r="3.5"/><circle cx="68" cy="46" r="3.5"/><circle cx="78" cy="46" r="3.5"/>
          <circle cx="46" cy="58" r="3.5"/><circle cx="56" cy="58" r="3.5"/><circle cx="68" cy="58" r="3.5"/><circle cx="78" cy="58" r="3.5"/>
          <circle cx="46" cy="70" r="3.5"/><circle cx="56" cy="70" r="3.5"/><circle cx="68" cy="70" r="3.5"/><circle cx="78" cy="70" r="3.5"/>
          <path d="M32 82 H92 V92 H32 Z"/>
        </g>
      </svg>
    </div>
    <div class="service">
      <p class="service-name">SNOW<br>REMOVAL</p>
      <svg class="service-icon" viewBox="0 0 124 124">
        <circle cx="62" cy="62" r="60" fill="var(--orange)"/>
        <path d="M36 66 C26 66 26 50 38 50 C38 36 58 32 64 44 C72 36 88 42 86 54 C96 54 96 66 86 66 Z" fill="none" stroke="var(--charcoal)" stroke-width="4" stroke-linejoin="round"/>
        <g stroke="var(--charcoal)" stroke-width="3" stroke-linecap="round">
          <path d="M48 78 V92 M41 85 H55 M43 80 L53 90 M53 80 L43 90"/>
          <path d="M74 78 V92 M67 85 H81 M69 80 L79 90 M79 80 L69 90"/>
        </g>
      </svg>
    </div>
  </section>

  <p class="promo">
    <span class="promo-value">25%</span>
    <span class="promo-off">OFF</span>
    <span class="promo-rest">THE FIRST MONTH</span>
  </p>

  <svg class="contact-arc" viewBox="0 0 900 140" aria-hidden="true">
    <path d="M60 140 C150 40 300 10 450 10 C600 10 750 40 840 140 Z" fill="var(--charcoal)" stroke="var(--white)" stroke-width="8"/>
  </svg>
  <div class="contact">
    <p class="contact-phone">(816) 555-0193</p>
    <p class="contact-web">www.gardelvista.com</p>
  </div>
</main>
</body>
</html>
```